Water Remediation and Restoration

Our company is in need of a trifold design for water damage industry.
This flyers main purpose is to help our company attain new accounts from Insurance and Management companies. This flyer will also be presented to apartment managers in the multi family housing industry, and insurance adjusters.

Our company provides clients with 24hr emergency services, including the following:
Emergency Mitigation
Water Extraction
Structural Drying
Dehumidication
Mold Removal
Asbestos and Environmental
Water Damage Restoration
Fire Damage Reconstruction
Contents Cleaning
Monitoring / Coordination
Antimicrobial Application
Smoke and Odor Removal

Target Market(s)

Insurance and Management Companies in Southern California

Industry/Entity Type

Industry

Font styles to use
Other font styles liked:
• Felix Titling

Colors
0455a3
ffffff
fbee3d

Requirements
Must have
• Number (800)517-2943
• License 2738460
Nice to have
• None Applicable
Should not have
• Any pictures from local competitors or busineses based in California

```html
<!DOCTYPE html>
<html lang="en">
<head>
<meta charset="utf-8">
<title>Water Remediation and Restoration</title>
<link rel="stylesheet" href="https://fonts.googleapis.com/css2?family=Cinzel:wght@400;500&family=Tinos:wght@400;700&display=swap">
<style>
  :root {
    --brand-blue: #0455a3;
    --band-blue: #3a55a6;
    --deep-navy: #1b2a6e;
    --white: #ffffff;
    --sun-yellow: #fbee3d;
    --gold: #f1c815;
    --ink: #111111;
  }
  * { margin: 0; padding: 0; box-sizing: border-box; }
  html, body { width: 869px; height: 1200px; overflow: hidden; background: #e9e9e9; }
  .flyer {
    position: relative;
    width: 869px;
    height: 1200px;
    overflow: hidden;
    background: linear-gradient(180deg, var(--sun-yellow) 40%, var(--gold) 100%);
  }
  .title-band {
    position: absolute; left: 0; top: 0; width: 869px; height: 244px;
    background: linear-gradient(180deg, #2f4d9e 0%, var(--band-blue) 60%, #4a63b0 100%);
    display: flex; flex-direction: column; align-items: center; justify-content: center;
  }
  .title {
    font-family: "Cinzel", serif;
    font-weight: 400;
    color: var(--white);
    font-size: 70px;
    line-height: 84px;
    text-align: center;
    letter-spacing: 1px;
  }
  .photo-row { position: absolute; top: 244px; left: 0; width: 869px; height: 330px; }
  .photo { position: absolute; top: 0; height: 330px; border-left: 8px solid var(--white); }
  .photo-pipes { left: 0; width: 282px; border-left: none;
    background: linear-gradient(135deg, #c94a2d 0%, #8c7c6a 45%, #cfc8bc 100%); }
  .photo-extraction { left: 282px; width: 296px;
    background: linear-gradient(180deg, #e6e6e2 0%, #b9c1cc 55%, #4a6bb0 100%); }
  .photo-hazmat { left: 578px; width: 291px;
    background: linear-gradient(160deg, #7d8488 0%, #c9ccd0 50%, #eef0f2 100%); }
  .swoosh { position: absolute; left: 0; top: 0; width: 869px; height: 1200px; }
  .portrait-ring {
    position: absolute; left: 40px; top: 630px; width: 382px; height: 382px;
    border-radius: 50%; background: var(--white); padding: 16px;
  }
  .portrait {
    width: 100%; height: 100%; border-radius: 50%;
    background: radial-gradient(circle at 50% 40%, #c9c9c9 0%, #8a8a8a 55%, #3f3f3f 100%);
  }
  .services {
    position: absolute; left: 462px; top: 620px; width: 400px;
    font-family: "Tinos", serif; color: var(--ink); font-size: 26px; line-height: 37.5px;
  }
  .services-intro { margin-bottom: 2px; line-height: 33px; }
  .service-list { list-style: none; }
  .service-list li::before { content: "\2022"; margin: 0 10px 0 4px; }
  .contact {
    position: absolute; left: 0; top: 1090px; width: 462px; text-align: center;
    font-family: "Tinos", serif;
  }
  .phone { color: var(--deep-navy); font-weight: 700; font-size: 54px; line-height: 60px; }
  .license { color: var(--ink); font-size: 28px; line-height: 34px; }
</style>
</head>
<body>
<main class="flyer">
  <header class="title-band">
    <h1 class="title">Water Remediation<br>and Restoration</h1>
  </header>

  <section class="photo-row">
    <div class="photo photo-pipes" role="img" aria-label="Burst industrial pipes with water damage"></div>
    <div class="photo photo-extraction" role="img" aria-label="Technician extracting water from carpet"></div>
    <div class="photo photo-hazmat" role="img" aria-label="Worker in protective suit handling remediation equipment"></div>
  </section>

  <svg class="swoosh" viewBox="0 0 869 1200" aria-hidden="true">
    <defs>
      <linearGradient id="fill-yellow" x1="0" y1="0" x2="0" y2="1">
        <stop offset="0" stop-color="#fbee3d"/>
        <stop offset="1" stop-color="#f1c815"/>
      </linearGradient>
    </defs>
    <path d="M0,560 C230,520 520,455 869,470 L869,560 C520,520 260,600 0,650 Z" fill="#3a55a6"/>
    <path d="M0,560 C230,520 520,455 869,470" fill="none" stroke="#ffffff" stroke-width="6"/>
    <path d="M0,650 C260,600 520,520 869,560 L869,1200 L0,1200 Z" fill="url(#fill-yellow)"/>
  </svg>

  <div class="portrait-ring">
    <div class="portrait" role="img" aria-label="Person looking through a window into a cleanroom"></div>
  </div>

  <section class="services">
    <p class="services-intro">Our company provides clients with 24hr emergency services, including the following:</p>
    <ul class="service-list">
      <li>Emergency Mitigation</li>
      <li>Water Extraction</li>
      <li>Structural Drying</li>
      <li>Dehumidication</li>
      <li>Mold Removal</li>
      <li>Asbestos and Environmental</li>
      <li>Water Damage Restoration</li>
      <li>Fire Damage Reconstruction</li>
      <li>Contents Cleaning</li>
      <li>Monitoring / Coordination</li>
      <li>Antimicrobial Application</li>
      <li>Smoke and Odor Removal</li>
    </ul>
  </section>

  <footer class="contact">
    <p class="phone">(800)517-2943</p>
    <p class="license">License 2738460</p>
  </footer>
</main>
</body>
</html>
```